A clean crisp business card for a Landscape Construction company. Designed to be easy to read contact/ info and also be appealing/interesting, unlike a traditional business card.

Industry/Entity Type

Landscape Construction

Contact Information for Business Card

Company name : Bramblecrest Landscape Construction, phone number: (877) 62Vales, website:Bramblecrestlandscapes.example, Email, sales@bramblecrestlandscapes.example

Requirements
Nice to have
• Luxurious finishes/ details…. Icons or emblems next to contact info
Should not have
• Clipart or general pictures

```html
<!DOCTYPE html>
<html lang="en">
<head>
<meta charset="utf-8">
<title>Bramblecrest Landscape Construction – Business Card</title>
<link rel="stylesheet" href="https://fonts.googleapis.com/css2?family=Josefin+Sans:wght@300;400;600;700&display=swap">
<style>
  :root {
    --leaf-green: #9dca3c;
    --wave-blue: #246bb5;
    --card-black: #000000;
    --paper: #ffffff;
    --ink-light: #ffffff;
  }
  * { margin: 0; padding: 0; box-sizing: border-box; }
  html, body { width: 1200px; height: 1000px; overflow: hidden; background: var(--paper); }
  .canvas { position: relative; width: 1200px; height: 1000px; font-family: "Josefin Sans", sans-serif; }
  .card { position: absolute; left: 280px; width: 640px; height: 365px; background: var(--card-black); overflow: hidden; }
  .card--front { top: 107px; }
  .card--back { top: 527px; }
  .card__waves { position: absolute; inset: 0; width: 640px; height: 365px; }
  .wave-green { fill: var(--leaf-green); }
  .wave-blue { fill: var(--wave-blue); }

  .header { position: absolute; left: 188px; top: 44px; color: var(--ink-light); }
  .header__name { font-size: 27px; font-weight: 700; letter-spacing: 1.5px; line-height: 1; }
  .header__tagline { font-size: 17px; font-weight: 300; letter-spacing: 0.8px; margin-top: 6px; }

  .brand { position: absolute; text-align: center; color: var(--leaf-green); font-weight: 600; }
  .brand--small { left: 18px; width: 206px; top: 232px; }
  .brand--small .brand__name { font-size: 22px; letter-spacing: 1px; line-height: 1; }
  .brand--small .brand__sub { font-size: 10px; letter-spacing: 1.4px; margin-top: 6px; }
  .brand--small .brand__dot { width: 40px; height: 40px; border-radius: 50%; background: var(--wave-blue); margin: 0 auto 14px; }
  .brand--large { left: 0; width: 640px; top: 196px; }
  .brand--large .brand__name { font-size: 40px; letter-spacing: 1.5px; }
  .brand--large .brand__sub { font-size: 15px; letter-spacing: 3px; margin-top: 8px; }

  .contacts { position: absolute; left: 238px; top: 213px; list-style: none; }
  .contact { display: flex; align-items: center; height: 41px; color: var(--ink-light); font-size: 17px; font-weight: 400; letter-spacing: 0; white-space: nowrap; }
  .contact__icon { width: 36px; height: 36px; margin-right: 14px; flex: none; }
  .contact__icon circle { fill: none; stroke: var(--leaf-green); stroke-width: 1.5; }
  .contact__icon .glyph { fill: none; stroke: var(--leaf-green); stroke-width: 1.6; stroke-linecap: round; stroke-linejoin: round; }
</style>
</head>
<body>
<main class="canvas">

  <section class="card card--front" aria-label="Business card front">
    <svg class="card__waves" viewBox="0 0 640 365" aria-hidden="true">
      <path class="wave-green" d="M0,0 H640 V66 C520,82 380,150 220,141 C120,136 40,102 0,60 Z"/>
      <path class="wave-blue" d="M0,60 C40,102 120,136 220,141 C380,150 520,82 640,66 V74 C520,98 380,178 220,176 C110,175 35,132 0,86 Z"/>
    </svg>

    <div class="header">
      <div class="header__name">BRAMBLECREST</div>
      <div class="header__tagline">LANDSCAPE CONSTRUCTION</div>
    </div>

    <div class="brand brand--small">
      <div class="brand__dot"></div>
      <div class="brand__name">BRAMBLECREST</div>
      <div class="brand__sub">LANDSCAPE CONSTRUCTION</div>
    </div>

    <ul class="contacts">
      <li class="contact">
        <svg class="contact__icon" viewBox="0 0 36 36" aria-hidden="true">
          <circle cx="18" cy="18" r="16.5"/>
          <path class="glyph" d="M12,11 l3,-1 2,4 -2,1.5 c1,2.5 2.5,4 5,5 l1.5,-2 4,2 -1,3 c-7,0 -12.5,-5.5 -12.5,-12.5 z"/>
          <path class="glyph" d="M20,10 a6,6 0 0 1 6,6 M20,13 a3,3 0 0 1 3,3"/>
        </svg>
        <span>(877) 62Vales</span>
      </li>
      <li class="contact">
        <svg class="contact__icon" viewBox="0 0 36 36" aria-hidden="true">
          <circle cx="18" cy="18" r="16.5"/>
          <rect class="glyph" x="10" y="12.5" width="16" height="11"/>
          <path class="glyph" d="M10,12.5 l8,6.5 8,-6.5"/>
        </svg>
        <span>bramblecrestlandscapes.example</span>
      </li>
      <li class="contact">
        <svg class="contact__icon" viewBox="0 0 36 36" aria-hidden="true">
          <circle cx="18" cy="18" r="16.5"/>
          <circle class="glyph" cx="18" cy="18" r="8.5"/>
          <ellipse class="glyph" cx="18" cy="18" rx="3.5" ry="8.5"/>
          <path class="glyph" d="M9.5,18 H26.5 M11,13.5 H25 M11,22.5 H25"/>
        </svg>
        <span>sales@bramblecrestlandscapes.example</span>
      </li>
    </ul>
  </section>

  <section class="card card--back" aria-label="Business card back">
    <svg class="card__waves" viewBox="0 0 640 365" aria-hidden="true">
      <path class="wave-green" d="M0,0 H640 C520,10 380,45 240,58 C120,68 40,40 0,0 Z"/>
      <path class="wave-blue" d="M0,0 C40,40 120,68 240,58 C380,45 520,10 640,0 V4 C520,22 380,80 240,88 C120,94 35,55 0,10 Z"/>
      <path class="wave-blue" d="M0,365 C150,330 330,272 460,270 C560,269 620,330 640,358 V365 Z"/>
      <path class="wave-green" d="M0,365 C170,345 340,300 460,298 C560,297 610,335 640,365 Z"/>
    </svg>

    <div class="brand brand--large">
      <div class="brand__name">BRAMBLECREST</div>
      <div class="brand__sub">LANDSCAPE CONSTRUCTION</div>
    </div>
  </section>

</main>
</body>
</html>
```